Harlow Ridge Growers and Nursery needs a business street sign.

I have three businesses located at the same address: The Harlow Ridge Growers & Nursery, The Bramble Nook, and The Quarry Commons. I am looking for a 4’ x 8’ street sign to represent all three businesses as one retail experience. It needs to be eye catching yet simple enough that people can fully read it while driving by. I have logos for the greenhouse and village however I do not have anything for The Bramble Nook. I’m looking for some type of font that’s similar or in between the two attached logos for The Bramble Nook.

• Horizontal Sign, Eye catching, yet simple design so people see it while driving by.
• Horizontal Sign
• I’m open to the design being both vertical and horizontal. Please provide both options

```html
<!DOCTYPE html>
<html lang="en">
<head>
<meta charset="utf-8">
<title>Harlow Ridge Street Sign</title>
<link rel="stylesheet" href="https://fonts.googleapis.com/css2?family=Montserrat:wght@800&display=swap">
<style>
  :root {
    --backdrop: #e4e2dd;
    --sign-face: #f8f7f4;
    --frame-red: #e1262b;
    --divider: #a98466;
    --nursery-green: #1f7a45;
    --commons-brown: #a8402c;
    --nook-black: #1d1b19;
    --board-tan: #c79a62;
    --board-ink: #3a2a1a;
    --bloom-blue: #8fb0e3;
    --bloom-violet: #b58fce;
    --bloom-pink: #e3b7d8;
    --leaf-green: #5f9a4c;
  }
  * { margin: 0; padding: 0; box-sizing: border-box; }
  html, body { width: 1200px; height: 899px; overflow: hidden; background: var(--backdrop); }
  .canvas { position: relative; width: 1200px; height: 899px; }
  .sign {
    position: absolute; left: 30px; top: 181px; width: 1140px; height: 537px;
    background: var(--sign-face);
    box-shadow: 0 2px 6px rgba(0,0,0,.12);
    overflow: hidden;
    font-family: "Montserrat", sans-serif; font-weight: 800;
  }
  .sign-frame { position: absolute; inset: 0; }
  .floral {
    position: absolute;
  }
  .floral--corner-left {
    left: 0; top: 0; width: 90px; height: 170px;
    background: linear-gradient(160deg, var(--bloom-violet), var(--bloom-blue) 45%, rgba(143,176,227,0) 100%);
    border-radius: 0 0 60px 0; opacity: .75;
  }
  .floral--corner-right {
    right: 0; top: 0; width: 110px; height: 150px;
    background: linear-gradient(200deg, var(--bloom-pink), var(--bloom-violet) 40%, rgba(181,143,206,0) 100%);
    border-radius: 0 0 0 70px; opacity: .75;
  }
  .floral--bouquet {
    right: 0; bottom: 0; width: 660px; height: 310px;
    background: radial-gradient(ellipse at 68% 62%, var(--bloom-blue) 0%, var(--bloom-violet) 38%, var(--leaf-green) 62%, rgba(95,154,76,0) 78%),
                linear-gradient(0deg, var(--bloom-pink) 0%, rgba(227,183,216,0) 30%);
    border-radius: 100% 0 0 0 / 100% 0 0 0;
    opacity: .85;
  }
  .cell { position: absolute; display: flex; flex-direction: column; justify-content: center; align-items: center; text-align: center; }
  .cell--nursery { left: 60px; top: 60px; width: 500px; height: 235px; }
  .cell--commons { left: 575px; top: 60px; width: 520px; height: 180px; }
  .cell--nook { left: 60px; top: 305px; width: 500px; height: 180px; }
  .nursery-name { color: var(--nursery-green); font-size: 62px; line-height: 1; letter-spacing: -1px; }
  .nursery-sub { color: var(--nursery-green); font-size: 23px; line-height: 1.3; letter-spacing: 1px; text-transform: uppercase; margin-top: 8px; }
  .commons-name { color: var(--commons-brown); font-size: 60px; line-height: 1.05; }
  .nook-name { color: var(--nook-black); font-size: 68px; line-height: 1.05; text-transform: uppercase; letter-spacing: 2px; }
  .explore-board {
    position: absolute; left: 862px; top: 300px; width: 160px; height: 170px;
    background: var(--board-tan); border-radius: 6px;
    transform: rotate(-4deg);
    display: flex; align-items: center; justify-content: center; text-align: center;
    color: var(--board-ink); font-size: 30px; line-height: 1.1; text-transform: uppercase;
  }
</style>
</head>
<body>
<main class="canvas">
  <section class="sign" aria-label="Shared street sign for three businesses">
    <div class="floral floral--corner-left" role="img" aria-label="Watercolour blue and violet flowers in the corner"></div>
    <div class="floral floral--corner-right" role="img" aria-label="Watercolour pink and violet flowers in the corner"></div>
    <div class="floral floral--bouquet" role="img" aria-label="Bouquet of blue hellebores, violet blooms and green leaves"></div>

    <svg class="sign-frame" width="1140" height="537" viewBox="0 0 1140 537" aria-hidden="true">
      <rect x="48" y="39" width="1064" height="454" rx="22" fill="none" stroke="var(--frame-red)" stroke-width="6"/>
      <line x1="565" y1="77" x2="565" y2="459" stroke="var(--divider)" stroke-width="2"/>
      <line x1="84" y1="299" x2="560" y2="299" stroke="var(--divider)" stroke-width="2"/>
    </svg>

    <div class="cell cell--nursery">
      <p class="nursery-name">Harlow Ridge</p>
      <p class="nursery-sub">Growers &amp; Nursery</p>
    </div>
    <div class="cell cell--commons">
      <p class="commons-name">Quarry<br>Commons</p>
    </div>
    <div class="cell cell--nook">
      <p class="nook-name">Bramble<br>Nook</p>
    </div>

    <div class="explore-board">Explore<br>Our<br>Shops</div>
  </section>
</main>
</body>
</html>
```